New Branding Business Card Design

Redesign business card according to new branding update.

** The design received so far are single color + BLACK.
I'd encourage designer to use different tones of blue / purple as described in the Designer Brief color palette

Target Market(s)

International

Industry/Entity Type

Medical Equipment

Contact Information for Business Card

Logo on one side (Designer can decide if they want to move certain info from the other side to save space)

Main body info (company name, individual name in both English and Chinese, contact info etc) on the other
Prefer a 'cleaner' layout - vs 'all over the place'
Prefer flush left alignment

Font styles to use
Sans Serif

Requirements
Must have
• Key info
• (Company name (English)): VORAM (HK) Limited
• (Name (English)): Marcus L. Pryde
• (Credential): FCPA, FHKSI
• (Title): Founder, Managing Director & CEO
• For the following info, designers decide whether to use colon or no colon, stroke separator, or use icon gfx for T (for telephone fixed line, M for mobile etc.)
• T: +852 3517 VORAM / +852 3517 4062
• M: +852 6243 7719 / + 86 139 2745 3186
• E: marcus.l.pryde@voram-example.hk
Nice to have
• Depending on the space and spacing available designers can add or use fuller title and other info
• Title: Chairman of the Executive Committee, Founder, Managing Director & CEO
• (Name (Chinese)): 林書恒
Should not have
• One of our business entities a long company name that cannot be broken into 2 lines
• makes vertical implementation almost impossible

```html
<!DOCTYPE html>
<html lang="en">
<head>
<meta charset="utf-8">
<title>VORAM (HK) Limited — Business Card</title>
<link href="https://fonts.googleapis.com/css2?family=Montserrat:wght@500;600;700&family=Noto+Sans+TC:wght@500&display=swap" rel="stylesheet">
<style>
  :root {
    --brand-purple: #57287f;
    --ink: #2b2b2b;
    --ink-soft: #444444;
    --paper: #ffffff;
    --backdrop: #e9e8ec;
    --icon-dark: #2e2e30;
  }
  * { box-sizing: border-box; margin: 0; padding: 0; }
  html, body {
    width: 1200px; height: 900px; overflow: hidden;
    background: var(--backdrop);
    font-family: "Montserrat", sans-serif;
  }
  .sheet {
    width: 1200px; height: 900px;
    display: flex; flex-direction: column; align-items: center; justify-content: center;
    gap: 36px;
  }
  .card {
    width: 700px; height: 400px;
    background: var(--paper);
    box-shadow: 0 6px 22px rgba(0,0,0,0.18);
    position: relative; overflow: hidden;
  }

  /* Brand lockup */
  .brand {
    display: flex; align-items: center; gap: 14px;
  }
  .brand-square {
    width: 38px; height: 38px; border-radius: 7px;
    background: var(--brand-purple);
  }
  .brand-name {
    font-weight: 700; font-size: 24px; letter-spacing: 0.2px;
    color: var(--brand-purple);
  }

  /* Front */
  .card-front { display: flex; align-items: center; justify-content: center; }

  /* Back */
  .card-back { display: flex; }
  .brand-panel {
    width: 320px; height: 100%;
    background: var(--brand-purple);
    display: flex; align-items: center; justify-content: center;
  }
  .brand-panel .brand-square { background: var(--paper); }
  .brand-panel .brand-name { color: var(--paper); font-size: 21px; }

  .details {
    flex: 1; padding: 58px 46px 0 46px;
    display: flex; flex-direction: column;
  }
  .portrait-slot {
    width: 54px; height: 46px; border-radius: 8px;
    background: var(--icon-dark);
    margin-bottom: 14px;
  }
  .person-name {
    font-weight: 700; font-size: 22px; color: var(--brand-purple);
    display: flex; align-items: baseline; gap: 10px;
  }
  .person-name-zh {
    font-family: "Noto Sans TC", sans-serif; font-weight: 500;
    font-size: 22px;
  }
  .credentials { font-size: 13px; font-weight: 500; color: var(--ink); margin-top: 6px; }
  .job-title { font-size: 12px; font-weight: 500; color: var(--ink); margin-top: 4px; }
  .divider {
    height: 1px; background: var(--brand-purple);
    margin: 26px 0 30px; width: 100%;
  }
  .contact-list { list-style: none; display: flex; flex-direction: column; gap: 11px; }
  .contact-item {
    display: flex; align-items: center; gap: 12px;
    font-size: 11.5px; font-weight: 500; color: var(--ink-soft);
  }
  .contact-icon { width: 16px; height: 16px; flex: none; fill: var(--icon-dark); }
</style>
</head>
<body>
<main class="sheet">

  <section class="card card-front" aria-label="Card front">
    <div class="brand">
      <span class="brand-square"></span>
      <span class="brand-name">VORAM (HK) Limited</span>
    </div>
  </section>

  <section class="card card-back" aria-label="Card back">
    <div class="brand-panel">
      <div class="brand">
        <span class="brand-square"></span>
        <span class="brand-name">VORAM (HK) Limited</span>
      </div>
    </div>

    <div class="details">
      <div class="portrait-slot" role="img" aria-label="Portrait placeholder"></div>
      <h1 class="person-name">Marcus L. Pryde <span class="person-name-zh">林書恒</span></h1>
      <p class="credentials">FCPA, FHKSI</p>
      <p class="job-title">Founder, Managing Director &amp; CEO</p>
      <div class="divider"></div>
      <ul class="contact-list">
        <li class="contact-item">
          <svg class="contact-icon" viewBox="0 0 24 24" aria-hidden="true"><path d="M6.6 10.8a15.1 15.1 0 0 0 6.6 6.6l2.2-2.2c.3-.3.7-.4 1-.2 1.1.4 2.3.6 3.6.6.6 0 1 .4 1 1V20c0 .6-.4 1-1 1A17 17 0 0 1 3 4c0-.6.4-1 1-1h3.5c.6 0 1 .4 1 1 0 1.3.2 2.5.6 3.6.1.3 0 .7-.2 1z"/></svg>
          <span>+852 3517 VORAM / +852 3517 4062</span>
        </li>
        <li class="contact-item">
          <svg class="contact-icon" viewBox="0 0 24 24" aria-hidden="true"><path d="M8 2h8a2 2 0 0 1 2 2v16a2 2 0 0 1-2 2H8a2 2 0 0 1-2-2V4a2 2 0 0 1 2-2zm0 3v12h8V5zm4 13.5a1 1 0 1 0 0 2 1 1 0 0 0 0-2z"/></svg>
          <span>+852 6243 7719 / + 86 139 2745 3186</span>
        </li>
        <li class="contact-item">
          <svg class="contact-icon" viewBox="0 0 24 24" aria-hidden="true"><path d="M3 5h18a1 1 0 0 1 1 1v12a1 1 0 0 1-1 1H3a1 1 0 0 1-1-1V6a1 1 0 0 1 1-1zm1 2.3V17h16V7.3l-8 5.3zM5.2 7 12 11.5 18.8 7z"/></svg>
          <span>marcus.l.pryde@voram-example.hk</span>
        </li>
      </ul>
    </div>
  </section>

</main>
</body>
</html>
```